Splash page redesign - http://thebrightwaterhomeadvisors.com/

I would like to modify my website splash page to include my nestory reviews in a somewhat prominent way without making the landing page too busy. My earned media gets me a lot clients and it needs to be available and noticeable without being TOO much.
I also want to change the tag line of the web site from: OVER $100,000,000 IN CLOSED SHORT SALE TRANSACTIONS to : BECAUSE YOU NEED A SHORT SALE COMPANY, NOT JUST AN AGENT. And the second line to be replaced with: OVER $150,000,000 IN CLOSED SHORT SALES AND WE COVER ALL OF MARYLAND
I really need the Nestory reviews to stand out and be seen when the page loads and people dont have to scroll down. LOVE the opt in for the free ebook near the top as well
Industry/Entity Type
Real Estate
Number of Pages Required
2 page
Font styles to use
Requirements
Must have
- I really need the Nestory reviews to stand out and be seen when the page loads and people dont have to scroll down. LOVE the opt in for the free ebook near the top as well
Nice to have
- mentioned above

```html
<!DOCTYPE html>
<html lang="en">
<head>
<meta charset="utf-8">
<title>Brightwater Home Advisors</title>
<link href="https://fonts.googleapis.com/css2?family=Source+Sans+3:ital,wght@0,400;0,600;0,700;0,800;1,700&family=Lato:ital,wght@0,400;0,700;1,400;1,700&family=Tinos:wght@400;700&display=swap" rel="stylesheet">
<style>
:root{
  --black:#000;
  --teal:#4c7282;
  --teal-mid:#6b8e9c;
  --teal-light:#86a1ad;
  --red:#b5202e;
  --white:#fff;
  --paper:#efefef;
  --review-bg:#dcdcdc;
  --ink:#222;
  --muted:#555;
  --gold:#f3b61f;
}
*{box-sizing:border-box;margin:0;padding:0}
html,body{width:670px;height:1200px;overflow:hidden;background:var(--white)}
body{position:relative;font-family:"Lato",sans-serif;color:var(--ink)}
.abs{position:absolute}

/* header */
.site-header{left:0;top:0;width:670px;height:58px;background:var(--black);border-top:3px solid #444}
.contact-tab{left:430px;top:0;width:160px;height:15px}
.contact-item{top:4px;font:700 6.5px "Tinos",serif;color:var(--white);white-space:nowrap}
.brand{top:18px;display:flex;align-items:center;gap:4px;font:800 11px "Source Sans 3",sans-serif;color:var(--white);letter-spacing:.3px;white-space:nowrap}
.brand i{display:block;width:9px;height:9px;background:var(--red)}
.brand-primary{left:81px}
.brand-secondary{left:150px}
.main-nav{right:80px;top:35px;display:flex;gap:15px;font:700 6.6px "Source Sans 3",sans-serif;text-transform:uppercase;color:var(--white);white-space:nowrap}
.main-nav .active{color:#e0303e}

/* hero */
.hero{left:0;top:58px;width:670px;height:301px;background:linear-gradient(180deg,#47505a 0%,#6a6e6a 40%,#5f7a45 70%,#6d6a60 100%)}
.hero-title{left:0;top:183px;width:670px;text-align:center;color:var(--white);font:700 19px/18px "Source Sans 3",sans-serif;text-transform:uppercase;text-shadow:0 1px 3px rgba(0,0,0,.6)}
.hero-sub{left:0;top:221px;width:670px;text-align:center;color:var(--white);font:italic 700 12.5px "Source Sans 3",sans-serif;text-shadow:0 1px 3px rgba(0,0,0,.6)}

/* ebook */
.ebook{left:0;top:359px;width:670px;height:85px;background:var(--black)}
.ebook-label{left:112px;top:395px;font:700 12.5px "Tinos",serif;color:var(--white)}
.field{height:17px;background:var(--white);border:1px solid #ccc;font:400 6.5px "Tinos",serif;color:#555;padding:5px 6px;white-space:nowrap;overflow:hidden}
.req-note{left:395px;top:419px;font:italic 400 5px "Lato",sans-serif;color:var(--white)}
.send-btn{left:506px;top:412px;width:84px;height:21px;background:var(--red);border-radius:3px;color:var(--white);font:700 7px "Source Sans 3",sans-serif;display:flex;align-items:center;justify-content:center;gap:4px}

/* mission */
.mission{left:0;top:444px;width:670px;height:326px;background:var(--paper)}
.mission-title{left:81px;top:507px;font:700 10.2px/12.5px "Source Sans 3",sans-serif;color:var(--red)}
.mission-body{left:81px;top:536px;width:246px;font:400 6.5px/10px "Lato",sans-serif;color:var(--ink)}
.mission-sign{left:81px;top:630px;font:italic 700 6.2px/8.5px "Lato",sans-serif}
.video{left:342px;top:498px;width:248px;height:159px;background:#1a1a1a}
.video-bar{left:0;top:0;width:248px;height:19px;background:#111;color:var(--white);font:400 7.5px "Lato",sans-serif;padding:5px 8px}
.video-frame{left:0;top:19px;width:248px;height:140px;background:linear-gradient(135deg,#5a3d2a 0%,#8a6a4a 35%,#6e83b8 70%,#3c4d7a 100%)}
.quick-links{left:81px;top:677px}
.quick-links text{font:italic 700 9.6px "Tinos",serif;fill:var(--white)}

/* reviews */
.reviews{left:0;top:770px;width:670px;height:254px;background:var(--review-bg)}
.reviews-title{left:0;top:795px;width:670px;text-align:center;font:700 10px "Source Sans 3",sans-serif;color:var(--red)}
.review-card{left:114px;top:812px;width:442px;height:142px;background:var(--white);border-radius:14px}
.review-headline{left:0;top:50px;width:442px;text-align:center;font:italic 700 10px "Lato",sans-serif}
.review-text{left:32px;top:68px;width:378px;text-align:center;font:italic 400 6.1px/10px "Lato",sans-serif;color:#333}
.reviewer{left:0;top:978px;width:670px;text-align:center;font:700 8.5px "Tinos",serif;color:var(--teal)}
.reviewer-note{left:0;top:991px;width:670px;text-align:center;font:400 5.5px "Tinos",serif;color:#444}

/* footer */
.site-footer{left:0;top:1024px;width:670px;height:176px;background:var(--black)}
.footer-head{top:1049px;font:700 7.4px "Source Sans 3",sans-serif;color:var(--white);letter-spacing:.4px;text-transform:uppercase;border-bottom:1px solid #666;padding-bottom:4px}
.footer-links{top:1068px;list-style:none;font:400 5.2px/9.9px "Lato",sans-serif;color:var(--white);white-space:nowrap}
.footer-links li::before{content:"\25B8";font-size:4.5px;margin-right:3px}
.footer-links .two-line{line-height:6.2px;padding:1px 0 2px}
.footer-links .two-line span{display:block;padding-left:8px}
.contact-info{left:473px;top:1068px;font:400 5.6px/7.3px "Lato",sans-serif;color:var(--white);white-space:nowrap}
.contact-info b{font-weight:700;font-size:6.4px}
.contact-info .mail{color:#e0303e}
.copyright{right:80px;top:1186px;font:400 4.6px "Tinos",serif;color:#888}
</style>
</head>
<body>

<header class="abs site-header">
  <svg class="abs contact-tab" viewBox="0 0 160 15" width="160" height="15"><polygon points="0,0 160,0 154,15 6,15" fill="#555"/></svg>
  <div class="abs brand brand-primary"><i></i>Keystone</div>
  <div class="abs brand brand-secondary">Brightwater</div>
  <nav class="abs main-nav">
    <span class="active">Welcome</span><span>About Us</span><span>Testimonials &#9662;</span><span>Short Sale Info &#9662;</span><span>Contact Us</span>
  </nav>
</header>
<span class="abs contact-item" style="left:452px">&#9742; 888-555-0142</span>
<span class="abs contact-item" style="left:506px">&#9993; dan@brightwaterhome.com</span>

<section class="abs hero" role="img" aria-label="Photo of a smiling family holding a sold sign in front of their house"></section>
<h1 class="abs hero-title">Because you need a short sale company,<br>not just an agent</h1>
<p class="abs hero-sub">Over $150,000,000 in closed short sales and we cover all of Maryland</p>

<section class="abs ebook">
  <svg class="abs" style="left:0;top:0" width="290" height="85" viewBox="0 0 290 85"><polygon points="0,0 288,0 256,85 0,85" fill="var(--teal)"/></svg>
</section>
<div class="abs ebook-label">FREE Short Sale Ebook</div>
<div class="abs field" style="left:295px;top:370px;width:188px">Name*</div>
<div class="abs field" style="left:485px;top:370px;width:105px">Phone</div>
<div class="abs field" style="left:295px;top:390px;width:188px">Email*</div>
<div class="abs field" style="left:485px;top:390px;width:105px">What is thirteen minus 6?*</div>
<div class="abs req-note">Fields marked with a * are required.</div>
<div class="abs send-btn"><svg width="8" height="8" viewBox="0 0 10 10"><polygon points="0,4 10,0 7,10 5,6" fill="#fff"/></svg>SEND</div>

<section class="abs mission"></section>
<h2 class="abs mission-title">IT’S NOT JUST OUR BUSINESS, ITS OUR MISSION.<br>Because we have been through this ourselves</h2>
<p class="abs mission-body">Our company exists solely to provide a dignified, NO COST exit strategy - executed in a way that most won’t even know your home was sold (we even successfully market without signs or lockboxes). I started our short sale company as a result of having our personal home and 10 investment properties foreclosed upon in 2008. My family endured the heavy handed tactics that banks use on homeowners. We provide a soft landing, with minimal impact, for people who no longer desire to keep their property, but owe more than its worth. Our services help you resolve this issue on your terms, not your lenders.</p>
<p class="abs mission-sign">President of The Brightwater Group<br>-Dan Whitmore</p>

<div class="abs video">
  <div class="abs video-bar">Commonly Asked Short Sale Questions</div>
  <svg class="abs" style="right:8px;top:5px" width="10" height="9" viewBox="0 0 10 9"><path d="M6 0 L10 4 L6 8 V5.5 C3 5.5 1.5 6.5 0 8.5 C0.5 5 2.5 3 6 2.5 Z" fill="#fff"/></svg>
  <div class="abs video-frame" role="img" aria-label="Video still of the company president answering common short sale questions"></div>
  <svg class="abs" style="left:112px;top:80px" width="24" height="18" viewBox="0 0 24 18"><rect width="24" height="18" rx="4" fill="rgba(0,0,0,.6)"/><polygon points="9,5 17,9 9,13" fill="#fff"/></svg>
</div>

<svg class="abs quick-links" width="509" height="40" viewBox="0 0 509 40">
  <path d="M8,0 H176 L156,40 H8 A8,8 0 0 1 0,32 V8 A8,8 0 0 1 8,0 Z" fill="var(--teal)"/>
  <polygon points="180,0 353,0 333,40 160,40" fill="var(--teal-mid)"/>
  <path d="M357,0 H501 A8,8 0 0 1 509,8 V32 A8,8 0 0 1 501,40 H337 Z" fill="var(--teal-light)"/>
  <text x="80" y="17" text-anchor="middle">Do We Qualify For a</text>
  <text x="80" y="29" text-anchor="middle">Short Sale?</text>
  <text x="256" y="23" text-anchor="middle">What is my Home Worth?</text>
  <text x="428" y="17" text-anchor="middle">Common Misconception</text>
  <text x="428" y="29" text-anchor="middle">&amp; Mistakes</text>
</svg>

<section class="abs reviews"></section>
<h2 class="abs reviews-title">NESTORY REVIEWS</h2>
<svg class="abs" style="left:80px;top:868px" width="16" height="30" viewBox="0 0 16 30"><polyline points="14,1 2,15 14,29" fill="none" stroke="#999" stroke-width="1.5"/></svg>
<svg class="abs" style="left:574px;top:868px" width="16" height="30" viewBox="0 0 16 30"><polyline points="2,1 14,15 2,29" fill="none" stroke="#999" stroke-width="1.5"/></svg>
<svg class="abs" style="left:321px;top:953px" width="30" height="20" viewBox="0 0 30 20"><polygon points="0,0 30,0 15,19" fill="#fff"/></svg>
<div class="abs review-card">
  <svg class="abs" style="left:178px;top:27px" width="86" height="17" viewBox="0 0 86 17">
    <g fill="var(--gold)">
      <polygon id="star" points="8.5,0 10.9,5.6 17,6.2 12.4,10.2 13.8,16.2 8.5,13 3.2,16.2 4.6,10.2 0,6.2 6.1,5.6"/>
      <use href="#star" x="17"/><use href="#star" x="34"/><use href="#star" x="51"/><use href="#star" x="68"/>
    </g>
  </svg>
  <div class="abs review-headline">Highly likely to recommend!</div>
  <p class="abs review-text">Dan knows exactly how to accomplish and complete the sale, no matter how difficult. He is intuitive, experienced, professional, and knows how it all works. In my case, with Harborline Bank, he had to represent my interest yet get it all done in the best way possible within the time frame of everyone: seller, buyer, and lender. He even arranged the connections for the buyer to get an outstanding home loan. I changed to Dan after initially using two other Realtors, but they did not know what Dan knows, and changing to Dan was the best decision i could have made. He should get an award for the best Realtor!</p>
</div>
<div class="abs reviewer">mbreez</div>
<div class="abs reviewer-note">Sold a Single Family home</div>

<footer class="abs site-footer">
  <svg class="abs" style="left:0;top:0" width="290" height="176" viewBox="0 0 290 176"><polygon points="0,0 284,0 253,176 0,176" fill="var(--teal)"/></svg>
</footer>
<div class="abs footer-head" style="left:81px;width:163px">Short Sale Group</div>
<svg class="abs" style="left:81px;top:1071px" width="164" height="110" viewBox="0 0 164 110">
  <rect width="163" height="60" fill="#fff"/>
  <rect x="12" y="12" width="40" height="36" rx="4" fill="#c8c8c8"/>
  <rect x="64" y="20" width="86" height="4" fill="#bbb"/><rect x="64" y="29" width="80" height="4" fill="#bbb"/><rect x="64" y="38" width="60" height="4" fill="#bbb"/>
  <rect y="67" width="45" height="41" fill="#fff"/>
  <circle cx="22.5" cy="85" r="12" fill="#1f4f8a"/>
  <rect x="51" y="67" width="112" height="37" fill="#fff"/>
  <circle cx="70" cy="85.5" r="12" fill="#7cb342"/>
  <rect x="90" y="80" width="60" height="4" fill="#d7c36a"/><rect x="90" y="88" width="40" height="4" fill="#f3b61f"/>
</svg>

<div class="abs footer-head" style="left:298px;width:74px">Pages</div>
<ul class="abs footer-links" style="left:298px">
  <li>Welcome</li><li>About Us</li><li>Testimonials</li><li>Short Sale Info</li><li>Contact Us</li>
</ul>
<div class="abs footer-head" style="left:386px;width:74px">Short Sale</div>
<ul class="abs footer-links" style="left:386px">
  <li>The Short Sale Process</li><li>Nine Reasons To Use Us</li><li>Common Misconceptions</li><li>Will I Qualify?</li><li>Questions You Must Ask</li><li>Avoid Foreclosure</li><li class="two-line">Short Sale versus<span>Foreclosure</span></li><li>What is Your Home Worth?</li><li>FSBO not Selling?</li><li>Informative Video</li>
</ul>
<div class="abs footer-head" style="left:473px;width:117px">Contact Us</div>
<div class="abs contact-info">
  <b>Dan Whitmore</b><br>Keystone Realty<br>Brightwater Home Advisors<br><br>
  <b>&#9742; 888-555-0142</b><br><b>&#9113; 866-555-0187</b><br>
  <span class="mail">&#9993; dan@brightwaterhome.com</span>
</div>
<div class="abs copyright">©2017 Brightwater Home Advisors. All rights reserved.</div>

</body>
</html>
```